Simple graphic for a book or slide presentation

We are looking for a style that suits the style of our book. It's title is Venture. Thriving boldly on uncertain ground. There will be more line drawing/graphics in the book but how you design this image will create the style for all the other simple graphics in the book (once we decide what they are). So this one design will lead to a few more to match the style of this one. We'd like the shape of the overall graphic (i.e the arrows and words/bubbles) to be circular (not a rounded square as appears in the sample attached). Perhaps the words don't need to be in ovals or bound by anything at all; perhaps they do - let's see what you see. We'd like you to choose a font or offer many different fonts you think will capture the practical yet unconventional tone of the book. The book is teaching that managing risks in life is a life-skill that can be learned. The section of the book where this graphic will be placed is called "the power of language" - basically we are saying that thoughts, words and actions create our culture and our destiny. This insight comes from Pranav Kelkari's famous quote:
Carefully watch your thoughts, for they become your words.
Manage and watch your words, for they will become your actions.
Consider and judge your actions, for they have become your habits.
Acknowledge and watch your habits, for they shall become your values.
Understand and embrace your values, for they become your destiny.

Please change the text in the middle of the graphic to say: The Human Culture Cycle

```html
<!DOCTYPE html>
<html lang="en">
<head>
<meta charset="utf-8">
<title>The Human Culture Cycle</title>
<link href="https://fonts.googleapis.com/css2?family=Open+Sans:wght@700;800&display=swap" rel="stylesheet">
<style>
  :root {
    --bg: #ffffff;
    --gap: #ffffff;
    --label: #ffffff;
    --title: #6d6d6d;
    --thoughts-outer: #212121;
    --thoughts-inner: #5f5f5f;
    --words-outer: #2b2b2b;
    --words-inner: #666666;
    --actions-outer: #353535;
    --actions-inner: #707070;
    --habits-outer: #535353;
    --habits-inner: #878787;
    --values-outer: #727272;
    --values-inner: #999999;
    --culture-outer: #939393;
    --culture-inner: #b0b0b0;
  }
  html, body {
    margin: 0;
    padding: 0;
    width: 1200px;
    height: 1000px;
    overflow: hidden;
    background: var(--bg);
  }
  .cycle-diagram {
    display: block;
    width: 1200px;
    height: 1000px;
  }
  .segment-outline {
    fill: none;
    stroke: var(--gap);
    stroke-width: 10;
    stroke-linejoin: miter;
    stroke-miterlimit: 10;
  }
  .stage-label {
    font-family: "Open Sans", Arial, sans-serif;
    font-weight: 700;
    font-size: 30px;
    fill: var(--label);
    letter-spacing: 1px;
  }
  .cycle-title {
    font-family: "Open Sans", Arial, sans-serif;
    font-weight: 700;
    font-size: 56px;
    fill: var(--title);
    text-anchor: middle;
  }
  .seg-thoughts .outer { fill: var(--thoughts-outer); }
  .seg-thoughts .inner { fill: var(--thoughts-inner); }
  .seg-words .outer { fill: var(--words-outer); }
  .seg-words .inner { fill: var(--words-inner); }
  .seg-actions .outer { fill: var(--actions-outer); }
  .seg-actions .inner { fill: var(--actions-inner); }
  .seg-habits .outer { fill: var(--habits-outer); }
  .seg-habits .inner { fill: var(--habits-inner); }
  .seg-values .outer { fill: var(--values-outer); }
  .seg-values .inner { fill: var(--values-inner); }
  .seg-culture .outer { fill: var(--culture-outer); }
  .seg-culture .inner { fill: var(--culture-inner); }
</style>
</head>
<body>
<svg class="cycle-diagram" viewBox="0 0 1200 1000" xmlns="http://www.w3.org/2000/svg" aria-labelledby="cycleTitle">
  <title id="cycleTitle">The Human Culture Cycle: thoughts, words, actions, habits, values, culture</title>
  <defs>
    <clipPath id="innerBand">
      <circle cx="600" cy="501" r="280"/>
    </clipPath>
    <path id="shape-thoughts" d="M558.7,138.3 A365,365 0 0 1 893.4,283.9 L873.0,376.6 L788.9,361.2 A235,235 0 0 0 573.4,267.5 L628.7,202.4 Z"/>
    <path id="shape-words" d="M893.4,283.9 A365,365 0 0 1 934.7,646.5 L844.2,675.2 L815.5,594.7 A235,235 0 0 0 788.9,361.2 L873.0,376.6 Z"/>
    <path id="shape-actions" d="M934.7,646.5 A365,365 0 0 1 641.3,863.7 L571.3,799.6 L626.6,734.5 A235,235 0 0 0 815.5,594.7 L844.2,675.2 Z"/>
    <path id="shape-habits" d="M641.3,863.7 A365,365 0 0 1 306.6,718.1 L327.0,625.4 L411.1,640.8 A235,235 0 0 0 626.6,734.5 L571.3,799.6 Z"/>
    <path id="shape-values" d="M306.6,718.1 A365,365 0 0 1 265.3,355.5 L355.8,326.8 L384.5,407.3 A235,235 0 0 0 411.1,640.8 L327.0,625.4 Z"/>
    <path id="shape-culture" d="M265.3,355.5 A365,365 0 0 1 558.7,138.3 L628.7,202.4 L573.4,267.5 A235,235 0 0 0 384.5,407.3 L355.8,326.8 Z"/>
    <path id="labelTrack" d="M600,183 A318,318 0 1 1 600,819 A318,318 0 1 1 600,183"/>
  </defs>

  <g class="cycle-ring">
    <g class="seg-thoughts"><use href="#shape-thoughts" class="outer"/><use href="#shape-thoughts" class="inner" clip-path="url(#innerBand)"/></g>
    <g class="seg-words"><use href="#shape-words" class="outer"/><use href="#shape-words" class="inner" clip-path="url(#innerBand)"/></g>
    <g class="seg-actions"><use href="#shape-actions" class="outer"/><use href="#shape-actions" class="inner" clip-path="url(#innerBand)"/></g>
    <g class="seg-habits"><use href="#shape-habits" class="outer"/><use href="#shape-habits" class="inner" clip-path="url(#innerBand)"/></g>
    <g class="seg-values"><use href="#shape-values" class="outer"/><use href="#shape-values" class="inner" clip-path="url(#innerBand)"/></g>
    <g class="seg-culture"><use href="#shape-culture" class="outer"/><use href="#shape-culture" class="inner" clip-path="url(#innerBand)"/></g>
  </g>

  <g class="segment-outlines">
    <use href="#shape-thoughts" class="segment-outline"/>
    <use href="#shape-words" class="segment-outline"/>
    <use href="#shape-actions" class="segment-outline"/>
    <use href="#shape-habits" class="segment-outline"/>
    <use href="#shape-values" class="segment-outline"/>
    <use href="#shape-culture" class="segment-outline"/>
  </g>

  <g class="stage-labels">
    <text class="stage-label" text-anchor="middle" dominant-baseline="middle"><textPath href="#labelTrack" startOffset="9.6%">THOUGHTS</textPath></text>
    <text class="stage-label" text-anchor="middle" dominant-baseline="middle"><textPath href="#labelTrack" startOffset="25.7%">WORDS</textPath></text>
    <text class="stage-label" text-anchor="middle" dominant-baseline="middle"><textPath href="#labelTrack" startOffset="42.2%">ACTIONS</textPath></text>
    <text class="stage-label" text-anchor="middle" dominant-baseline="middle"><textPath href="#labelTrack" startOffset="59.4%">HABITS</textPath></text>
    <text class="stage-label" text-anchor="middle" dominant-baseline="middle"><textPath href="#labelTrack" startOffset="74.2%">VALUES</textPath></text>
    <text class="stage-label" text-anchor="middle" dominant-baseline="middle"><textPath href="#labelTrack" startOffset="91.9%">CULTURE</textPath></text>
  </g>

  <g class="cycle-heading" dominant-baseline="middle">
    <text class="cycle-title" x="600" y="373">THE</text>
    <text class="cycle-title" x="600" y="452">HUMAN</text>
    <text class="cycle-title" x="600" y="530">CULTURE</text>
    <text class="cycle-title" x="600" y="609">CYCLE</text>
  </g>
</svg>
</body>
</html>
```